Stalwart Noble Alloys Foundries Business Cards

Business Card Design Description
We are wanting to have a new business card designed for our company as we go to a convention. We want to balance business/Modern with elegance and beauty. Our company sells highend jewelry pieces. We want to utilize the colors of Black and Gold and have gold foiled fonts to be physically printed on the business cards.
We also would like to have space to write notes on the back side of the business card. When we meet people at jewelry conventions we would like to write notes if possible.
Here are websites and designs that we like the look and feel of these companies and you can use these as design ideas.
https://www.bellwynne.com
https://www.morvandel.com/en-us/home
Here is our company website link
www.stalwartnaf.com
I also up loaded two versions of our logo.
- Update 4.26.22
I have uploaded photos of a business card we like. this card has raised embossed letters that you can feel. the raise letters are like a plastic but we don't need to use that...I uploaded to show you that we like the experience of the client feeling the characters of the logo. we also would like to have the material as a satin or some material very soft.
- Maybe we can get designs with beautiful gold foiling and raised characters and logos. we like simplicity...not busy but an elegant design. We need to write notes and would like a section where we can write notes. but we want an elegant style and the client has an experience with the feel of the card when they touch the card.
Colors
- Main colors Black & Gold
- white or light colors for small notes section.
Specialty ideals and things we would like to see based on your design styles.
- raised fonts
- raised logos
- gold foiling
- satin/soft finish on the card material.
we are wanting to design a business card that looks elegant and clean. When the client is handed the business card we want them to physically experience the business card as well by touching the raised logos or fonts and the base material is soft satin. I hope this helps with further designs.
thank you all
We uploaded a new contact layout that we have designed in our office. we would like to see how this would look on your designs.
thank you
I just finished uploading the Contact Layout. the colors are just examples. please use this layout as an idea and use colors based on the feed back we have given each of you personally.
Contact Information for Business Card
we need an area to write notes, we would like to have our logos or the diamond of our logo or the business card to have embossed sections to the business card so when the customer touches the card they can feel the logo. we would also like sections of our business card to have gold foiling. we would also like to use a satin soft paper with our card. when the client touches the card its super soft and high quality
Requirements
Must have
- we would like to have our logos or the diamond of our logo or the business card to have embossed sections to the business card so when the customer touches the card they can feel the logo. we would also like sections of our business card to have gold foiling. we would also like to use a satin soft paper with our card. when the client touches the card its super soft and high quality
Nice to have
- we would like to have our logos or the diamond of our logo or the business card to have embossed sections to the business card so when the customer touches the card they can feel the logo. we would also like sections of our business card to have gold foiling.

```html
<!DOCTYPE html>
<html lang="en">
<head>
<meta charset="utf-8">
<title>Stalwart Noble Alloys Foundries – Business Cards</title>
<link rel="stylesheet" href="https://fonts.googleapis.com/css2?family=Cormorant+Garamond:wght@500&family=Carlito&display=swap">
<style>
  :root {
    --bg: #121212;
    --card: #232425;
    --gold: #c9a45c;
    --gold-light: #efe2c4;
    --gold-deep: #b08a3e;
    --ink: #1b1b1b;
  }
  html, body {
    margin: 0;
    width: 1200px;
    height: 1118px;
    overflow: hidden;
    background: var(--bg);
  }
  .stage {
    position: relative;
    width: 1200px;
    height: 1118px;
  }
  .card {
    position: absolute;
    left: 280px;
    width: 640px;
    height: 366px;
    background: var(--card);
    box-shadow: 0 20px 40px rgba(0,0,0,.55);
    overflow: hidden;
  }
  /* back side */
  .card-back { top: 110px; }
  .card-back .pattern-area {
    position: absolute;
    left: 0; top: 0;
    width: 100%;
    height: 63%;
    background: linear-gradient(135deg, #262728 0%, #2e2b25 50%, #262728 100%);
  }
  .card-back .foil-band {
    position: absolute;
    left: 0; bottom: 0;
    width: 100%;
    height: 37%;
    background: linear-gradient(100deg, var(--gold-deep) 0%, #d9c49a 35%, var(--gold-light) 50%, #d4b77a 70%, var(--gold-deep) 100%);
  }
  .card-back .band-rule {
    position: absolute;
    left: 268px;
    top: 30px;
    width: 104px;
    height: 2px;
    background: var(--ink);
  }
  /* front side */
  .card-front { top: 640px; }
  .brand {
    position: absolute;
    left: 44px;
    top: 38px;
    display: flex;
    align-items: center;
    gap: 10px;
    color: var(--gold);
  }
  .brand-mark {
    width: 10px;
    height: 10px;
    background: var(--gold);
  }
  .brand-name {
    font-family: "Cormorant Garamond", serif;
    font-weight: 500;
    font-size: 28px;
    line-height: 1;
  }
  .person {
    position: absolute;
    left: 44px;
    top: 104px;
    color: var(--gold);
  }
  .person-name {
    font-family: "Cormorant Garamond", serif;
    font-weight: 500;
    font-size: 27px;
    letter-spacing: .5px;
    margin: 0;
  }
  .person-role {
    font-family: "Cormorant Garamond", serif;
    font-weight: 500;
    font-size: 16px;
    margin: 0;
  }
  .contact {
    position: absolute;
    left: 44px;
    top: 178px;
    margin: 0;
    font-family: "Carlito", sans-serif;
    font-size: 15px;
    line-height: 1.35;
    color: var(--gold);
    font-style: normal;
  }
  .contact .gap { display: block; height: 8px; }
  .note-rules {
    position: absolute;
    right: 34px;
    top: 70px;
    width: 30px;
    height: 240px;
  }
</style>
</head>
<body>
<main class="stage">
  <section class="card card-back" aria-label="Card back">
    <div class="pattern-area" role="img" aria-label="Gold-foiled repeating diamond ornament pattern on black"></div>
    <div class="foil-band">
      <span class="band-rule"></span>
    </div>
  </section>

  <section class="card card-front" aria-label="Card front with notes space">
    <header class="brand">
      <span class="brand-mark" aria-hidden="true"></span>
      <span class="brand-name">Stalwart Noble Alloys</span>
    </header>
    <div class="person">
      <p class="person-name">EVAN THORSBY</p>
      <p class="person-role">Project Manager</p>
    </div>
    <address class="contact">
      2740 Linden Row NE<br>
      Marlow, OR 97390<br>
      P:&nbsp; (503) 555-0142
      <span class="gap"></span>
      E:&nbsp; hello@stalwartnaf.com<br>
      W: www.stalwartnaf.com
    </address>
    <svg class="note-rules" viewBox="0 0 30 240" aria-hidden="true">
      <line x1="6" y1="0" x2="6" y2="240" stroke="#c9a45c" stroke-width="3"/>
      <line x1="24" y1="20" x2="24" y2="240" stroke="#c9a45c" stroke-width="3"/>
    </svg>
  </section>
</main>
</body>
</html>
```